Tamkor, a service provider dedicated to improving the performance of a website

Tamkor offers optimization and performance improvement for all types of websites (showcase sites, e-commerce, ...), with the aim of improving their ranking on Vintrel and their customer transformation rate. The main benefits consist in optimizing the factors of a site. In addition, we also offer content creation (description of product sheets, services, ...), Vintrel Ads campaign management, migration version for Prestashop / Wordpress, etc. The design must be a fresh image, dynamic, why not "fun", but also serious. No favorite color, carte blanche on this point;)

```html
<!DOCTYPE html>
<html lang="fr">
<head>
<meta charset="utf-8">
<title>Tamkor – Business Card</title>
<link href="https://fonts.googleapis.com/css2?family=Montserrat:wght@400;500;700;800&display=swap" rel="stylesheet">
<style>
  :root{
    --brand-blue:#3a53ab;
    --brand-blue-deep:#2f4699;
    --paper:#ffffff;
    --ink:#1d1d24;
    --backdrop:#e9eaee;
  }
  *{margin:0;padding:0;box-sizing:border-box}
  html,body{width:1200px;height:900px;overflow:hidden}
  body{
    background:var(--backdrop);
    font-family:"Montserrat",sans-serif;
    position:relative;
  }
  .card{
    position:absolute;
    top:300px;
    width:520px;height:300px;
    border-radius:6px;
    overflow:hidden;
    box-shadow:0 10px 30px rgba(20,25,60,.18);
  }
  .card--front{left:60px;background:var(--paper)}
  .card--back{left:620px;background:var(--brand-blue)}

  .card__shape{position:absolute;inset:0;width:100%;height:100%}

  .identity{position:absolute;left:34px;top:34px}
  .identity__name{
    font-weight:700;font-size:20px;color:var(--brand-blue);letter-spacing:.2px;
  }
  .identity__role{
    font-weight:500;font-size:13px;color:var(--ink);margin-top:2px;
  }
  .identity__rule{
    width:14px;height:3px;background:var(--brand-blue);margin-top:18px;
  }

  .contacts{
    position:absolute;left:34px;top:146px;list-style:none;
  }
  .contacts__item{
    display:flex;align-items:center;gap:9px;
    font-size:13.5px;font-weight:500;color:var(--ink);
    line-height:1;margin-bottom:9px;
    white-space:nowrap;
  }
  .contacts__icon{width:13px;height:13px;flex:none}
  .contacts__item strong{color:var(--brand-blue);font-weight:700}

  .brand-name{
    position:absolute;
    font-weight:800;color:var(--paper);letter-spacing:-.5px;line-height:1;
    white-space:nowrap;
  }
  .card--front .brand-name{left:312px;top:166px;font-size:44px}
  .card--back .brand-name{left:0;right:0;top:130px;text-align:center;font-size:34px}

  .back-texture{position:absolute;inset:0;
    background:linear-gradient(135deg,var(--brand-blue) 0%,var(--brand-blue-deep) 100%)}
</style>
</head>
<body>

  <section class="card card--front" aria-label="Carte de visite, recto">
    <svg class="card__shape" viewBox="0 0 520 300" aria-hidden="true">
      <circle cx="520" cy="270" r="300" fill="var(--brand-blue)"/>
      <path d="M382 30 C302 50 252 110 244 190 C267 120 317 70 397 40 Z" fill="var(--paper)"/>
    </svg>

    <div class="identity">
      <p class="identity__name">Elian Marchetti</p>
      <p class="identity__role">Design Engineer</p>
      <div class="identity__rule"></div>
    </div>

    <ul class="contacts">
      <li class="contacts__item">
        <svg class="contacts__icon" viewBox="0 0 16 16" fill="none" stroke="var(--brand-blue)" stroke-width="1.5">
          <circle cx="8" cy="8" r="7"/>
          <path d="M5.5 4.5l1.5 0 .7 2-1 .8c.5 1 1.2 1.7 2.2 2.2l.8-1 2 .7v1.5c0 .5-.5 1-1 1C7.5 11.7 4.3 8.5 4.5 5.5c0-.5.5-1 1-1z" fill="var(--brand-blue)" stroke="none"/>
        </svg>
        06 21 57 39 84
      </li>
      <li class="contacts__item">
        <svg class="contacts__icon" viewBox="0 0 16 16" fill="none" stroke="var(--brand-blue)" stroke-width="1.5">
          <rect x="1.5" y="3.5" width="13" height="9" rx="1"/>
          <path d="M1.5 4l6.5 5 6.5-5"/>
        </svg>
        contact@tamkor.fr
      </li>
      <li class="contacts__item">
        <svg class="contacts__icon" viewBox="0 0 16 16" fill="none" stroke="var(--brand-blue)" stroke-width="1.4">
          <circle cx="8" cy="8" r="7" fill="var(--brand-blue)"/>
          <path d="M1 8h14M8 1c-2.5 2.5-2.5 11.5 0 14M8 1c2.5 2.5 2.5 11.5 0 14" stroke="var(--paper)" stroke-width="1"/>
        </svg>
        <span>www.<strong>tamkor</strong>.fr</span>
      </li>
    </ul>

    <p class="brand-name">Tamkor</p>
  </section>

  <section class="card card--back" aria-label="Carte de visite, verso">
    <div class="back-texture" role="img" aria-label="Motif embossé répété de la marque sur fond bleu"></div>
    <p class="brand-name">Tamkor</p>
  </section>

</body>
</html>
```